Animal Eye Clinic needs a Business card

We are a new veterinary ophthalmology practice (Tessaly Animal Eye Care) and we need a business card designed. We only see animal eyes - we are not a regular veterinary clinic. We already have a logo. We are looking for a professional, good looking business card to hand out to our clients. We are looking for something simple but professional and contemporary. Our logo is likely the only picture/graphic that needs to be on the card.
Updates

Contact Information for Business Card

Marisol Dunkley, BA, VMD, MVSc, DACVO
Veterinary Ophthalmologist

Phone: 250.418.3097
Email: tessalyanimaleyecare@mailbrook.net
Website: tessalyanimaleyecare.net
Address: 1840 Pellworth Rd
Brenmoor, NS, V4T 8M3

Colors

Designer to choose colors to be used in the design.

Requirements
Must have
• Our logo (attached)

```html
<!DOCTYPE html>
<html lang="en">
<head>
<meta charset="utf-8">
<title>Tessaly Animal Eye Care – Business Card</title>
<link href="https://fonts.googleapis.com/css2?family=Roboto:wght@400;500&family=Montserrat:wght@800&family=PT+Serif&family=Carlito&display=swap" rel="stylesheet">
<style>
  :root {
    --backdrop: #ccffcc;
    --card: #ffffff;
    --teal: #28c4a9;
    --ink: #111111;
    --rule: #000000;
    --ghost: #e4e4e4;
    --edge: #8a8a8a;
  }
  * { margin: 0; padding: 0; box-sizing: border-box; }
  html, body {
    width: 1182px; height: 1200px; overflow: hidden;
    background: var(--backdrop);
  }
  .card {
    position: absolute;
    width: 873px; height: 499px;
    background: var(--card);
    border: 1px solid var(--edge);
    border-radius: 66px 66px 0 0;
    overflow: hidden;
  }
  .card--front { left: 145px; top: 42px; }
  .card--back  { left: 138px; top: 584px; }

  .card__band {
    position: absolute; left: 0; right: 0; bottom: 0; height: 82px;
    background: var(--teal);
    border-radius: 18px 18px 0 0;
    z-index: 1;
  }
  .card__rule {
    position: absolute; left: 18px; right: 18px; top: 410px; height: 7px;
    background: var(--rule); border-radius: 4px;
    z-index: 2;
  }
  .watermark {
    position: absolute;
    background: radial-gradient(circle at 50% 50%, var(--ghost) 0%, #ececec 55%, rgba(236,236,236,0) 72%);
  }
  .card--front .watermark { left: 440px; top: -40px; width: 480px; height: 480px; }
  .card--back .watermark { left: 60px; top: 140px; width: 280px; height: 280px; }

  .brand__dot { position: absolute; border-radius: 50%; background: var(--teal); }
  .brand {
    position: absolute; white-space: nowrap;
    font-family: "Roboto", sans-serif; font-weight: 500; color: var(--teal);
  }
  .card--front .brand__dot { left: 100px; top: 130px; width: 112px; height: 112px; }
  .card--front .brand { left: 250px; top: 160px; font-size: 46px; line-height: 52px; }

  .card--back .brand__dot { left: 45px; top: 56px; width: 58px; height: 58px; }
  .card--back .brand { left: 116px; top: 71px; font-size: 22px; line-height: 26px; }

  .person { position: absolute; right: 33px; top: 46px; text-align: right; }
  .person__name {
    font-family: "Montserrat", sans-serif; font-weight: 800;
    font-size: 46px; line-height: 50px; color: var(--teal);
  }
  .person__credentials {
    font-family: "Roboto", sans-serif; font-size: 15px; color: var(--ink);
    margin-right: 6px; line-height: 18px;
  }
  .person__title {
    font-family: "PT Serif", serif; font-size: 22px; color: var(--ink); line-height: 28px;
  }
  .contact {
    position: absolute; right: 33px; top: 208px; text-align: right;
    font-family: "Carlito", sans-serif; font-size: 21px; line-height: 26.5px; color: var(--ink);
    list-style: none;
  }
</style>
</head>
<body>
  <section class="card card--front">
    <div class="watermark" role="img" aria-label="Faint enlarged clinic emblem in light grey"></div>
    <span class="brand__dot"></span>
    <p class="brand">Tessaly Animal Eye Care</p>
    <div class="card__rule"></div>
    <div class="card__band"></div>
  </section>

  <section class="card card--back">
    <div class="watermark" role="img" aria-label="Faint enlarged clinic emblem in light grey"></div>
    <span class="brand__dot"></span>
    <p class="brand">Tessaly Animal Eye Care</p>
    <div class="person">
      <h1 class="person__name">Marisol Dunkley</h1>
      <p class="person__credentials">BA, VMD, MVSc, DACVO</p>
      <p class="person__title">Veterinary Ophthalmologist</p>
    </div>
    <ul class="contact">
      <li>Phone: 250.418.3097</li>
      <li>Email: tessalyanimaleyecare@mailbrook.net</li>
      <li>Website: tessalyanimaleyecare.net</li>
      <li>Address: 1840 Pellworth Rd</li>
      <li>Brenmoor, NS, V4T 8M3</li>
    </ul>
    <div class="card__rule"></div>
    <div class="card__band"></div>
  </section>
</body>
</html>
```